Lumora vale- referral cards for new customers

Hey,

I would like 1 set of business cards with the following details:

10% off any sales / coupon code
Our phone number: 4702938165
Menu :Lumoravale.example (for the menu)
A line left blank to hand write an activation code: either on top or just on one side

Include the Lumora Vale logo ( your choice of black or white logo)
This card is to drive orders for people to order a cannabis order with Lumora Vale. Please make the logo a large part of the card on both sides.

Target Market(s)

People who consume cannabis 21 and up

Industry/Entity Type

Business

Contact Information for Business Card

This business card will be given to customers so they can then give it to other customers and generate referalls. We need this card to be elegant, impressionable, professional, and something worth keeping and passing to friends.

Font styles to use
Decorative
Script

Colors
33a6d7
85acd3
3176b5
0455a3
0592cd
85cae6
cee9f5
eaf1f7
757575

Requirements
Must have
• Our website
• Phone Number
• The 10% off an order
• Spot for activation code
Nice to have
• Eye catching design
• Look classy
• Textured feel or textured look
Should not have
• Do not look super cannabis heady
• Do not look attractive to children

```html
<!DOCTYPE html>
<html lang="en">
<head>
<meta charset="utf-8">
<title>Lumora Vale – Referral Cards</title>
<link href="https://fonts.googleapis.com/css2?family=Federo&family=Yesteryear&family=Raleway:wght@500&display=swap" rel="stylesheet">
<style>
  :root {
    --backdrop: #cfe2ea;
    --card-black: #050505;
    --card-white: #ffffff;
    --ink-white: #ffffff;
    --ink-black: #111111;
    --accent-olive: #5c5a2a;
    --mark-tone: #3f4a33;
    --shadow: rgba(20, 40, 50, 0.35);
  }
  * { box-sizing: border-box; margin: 0; padding: 0; }
  html, body { width: 1200px; height: 900px; overflow: hidden; }
  body { background: var(--backdrop); position: relative; font-family: "Raleway", sans-serif; }

  .card {
    position: absolute;
    width: 735px;
    height: 420px;
    border-radius: 26px;
    overflow: hidden;
    background: var(--card-black);
    box-shadow: 0 10px 22px var(--shadow);
  }
  .card--front { left: 70px; top: 25px; }
  .card--back { left: 395px; top: 455px; }

  /* Front */
  .brand-block {
    position: absolute; left: 0; right: 0; top: 60px;
    display: flex; flex-direction: column; align-items: center;
  }
  .brand-block__mark {
    width: 170px; height: 170px; border-radius: 50%;
    background: var(--mark-tone);
  }
  .brand-block__name {
    margin-top: 22px;
    font-family: "Federo", sans-serif;
    font-size: 48px; letter-spacing: 2px;
    color: var(--ink-white);
    white-space: nowrap;
  }
  .brand-block__site {
    margin-top: 14px;
    font-size: 15px; color: var(--ink-white);
  }

  /* Back */
  .back-art { position: absolute; inset: 0; }
  .offer {
    position: absolute; left: 30px; top: 70px;
    font-family: "Yesteryear", cursive;
    font-size: 30px; color: var(--ink-white);
    white-space: nowrap;
  }
  .offer__big { font-size: 42px; }
  .contact-list { position: absolute; left: 40px; top: 140px; list-style: none; }
  .contact-list__item {
    display: flex; align-items: center; gap: 10px;
    font-family: "Yesteryear", cursive;
    font-size: 26px; color: var(--ink-white); line-height: 40px;
    white-space: nowrap;
  }
  .contact-list__icon { width: 22px; height: 22px; flex: none; }
  .activation { position: absolute; left: 70px; top: 236px; }
  .activation__label {
    font-family: "Yesteryear", cursive;
    font-size: 26px; color: var(--ink-white);
  }
  .activation__field {
    margin-top: 6px;
    width: 270px; height: 46px;
    border: 3px solid var(--ink-white);
  }
  .referral-line {
    position: absolute; left: 70px; bottom: 22px;
    font-size: 15px; color: var(--ink-white);
    white-space: nowrap;
  }
  .brand-block--back { left: 360px; right: 0; top: 36px; }
  .brand-block--back .brand-block__mark { width: 150px; height: 150px; }
  .brand-block--back .brand-block__name { color: var(--ink-black); font-size: 44px; margin-top: 20px; }
</style>
</head>
<body>

  <section class="card card--front" aria-label="Card front">
    <div class="brand-block">
      <div class="brand-block__mark"></div>
      <div class="brand-block__name">Lumora Vale</div>
      <div class="brand-block__site">Lumoravale.example</div>
    </div>
  </section>

  <section class="card card--back" aria-label="Card back">
    <svg class="back-art" viewBox="0 0 735 420" width="735" height="420" aria-hidden="true">
      <circle cx="638" cy="100" r="340" fill="var(--accent-olive)"/>
      <circle cx="652" cy="88" r="340" fill="var(--card-white)"/>
    </svg>

    <div class="offer">The <span class="offer__big">10%</span> off an order</div>

    <ul class="contact-list">
      <li class="contact-list__item">
        <svg class="contact-list__icon" viewBox="0 0 24 24"><path fill="#fff" d="M6.6 10.8a15 15 0 0 0 6.6 6.6l2.2-2.2c.3-.3.7-.4 1-.2 1.1.4 2.3.6 3.6.6.6 0 1 .4 1 1V20c0 .6-.4 1-1 1A17 17 0 0 1 3 4c0-.6.4-1 1-1h3.5c.6 0 1 .4 1 1 0 1.3.2 2.5.6 3.6.1.3 0 .7-.2 1z"/></svg>
        <span>4702938165</span>
      </li>
      <li class="contact-list__item">
        <svg class="contact-list__icon" viewBox="0 0 24 24"><circle cx="12" cy="12" r="9.5" fill="none" stroke="#fff" stroke-width="2"/><path d="M2.5 12h19M12 2.5c3 3 3 16 0 19M12 2.5c-3 3-3 16 0 19" fill="none" stroke="#fff" stroke-width="1.6"/></svg>
        <span>Lumoravale.example</span>
      </li>
    </ul>

    <div class="activation">
      <div class="activation__label">activation code:</div>
      <div class="activation__field"></div>
    </div>

    <p class="referral-line">Order a cannabis with Lumoravale.example</p>

    <div class="brand-block brand-block--back">
      <div class="brand-block__mark"></div>
      <div class="brand-block__name">Lumora Vale</div>
    </div>
  </section>

</body>
</html>
```